themed infographic with multiple stats/charts

**Requires previous infographic experience and examples.**We need a skilled illustrator/designer to take an organized list of stats we've gathered related to the topic of investing and turn them into a professional looking, long, infographic with multiple sections, with a clear visual theme.We are not looking to match our branding guidelines. This will have a style and look all its own, with a goal of being compelling and sharable.Stats/content provided when we engage.

Target Market(s)

US customers, 25-45 years old

Colors

Designer to choose colors to be used in the design.

Requirements
Must have
• interesting theme that ties all the stats together, but separate panels for each stat
Should not have
• will not accept something that looks like cheap clip art

```html
<!DOCTYPE html>
<html lang="en">
<head>
<meta charset="utf-8">
<title>Investing in Your 20's, 30's, 40's, 50's and 60's</title>
<link href="https://fonts.googleapis.com/css2?family=Oswald:wght@300;400;500;600;700&display=swap" rel="stylesheet">
<style>
  :root {
    --navy: #0e2b4f;
    --gold: #ecb444;
    --gold-deep: #d9a23a;
    --sky: #00aeef;
    --white: #ffffff;
    --soft: #e6ebf2;
    --tick-grey: #8d99aa;
  }
  * { margin: 0; padding: 0; box-sizing: border-box; }
  html, body { width: 1200px; height: 2861px; overflow: hidden; }
  body {
    background: var(--navy);
    font-family: "Oswald", "Arial Narrow", sans-serif;
    color: var(--soft);
    position: relative;
  }
  .abs { position: absolute; }
  .condensed { display: inline-block; transform-origin: left top; white-space: nowrap; }

  .title-main {
    left: 50px; top: 58px;
    color: var(--gold); font-weight: 700; font-size: 168px; line-height: 1;
    letter-spacing: -2px; text-transform: uppercase;
    transform: scaleX(0.84);
  }
  .title-sub {
    left: 50px; top: 200px;
    color: var(--white); font-weight: 300; font-size: 112px; line-height: 1;
    letter-spacing: -3px;
    transform: scaleX(0.94);
  }

  .stage-head { display: flex; align-items: center; gap: 14px; }
  .stage-icon {
    width: 78px; height: 78px; border-radius: 50%;
    background: var(--gold); opacity: .9; flex: none;
  }
  .stage-title {
    color: var(--gold); font-weight: 600; font-size: 40px; line-height: 1;
    text-transform: uppercase; letter-spacing: -.5px;
  }

  .ticks { list-style: none; }
  .ticks li {
    position: relative; padding-left: 28px;
    font-size: 26px; font-weight: 400; line-height: 29px; margin-bottom: 7px;
    letter-spacing: -.4px;
  }
  .ticks li::before {
    content: ""; position: absolute; left: 0; top: 8px;
    width: 17px; height: 17px; border-radius: 50%; background: var(--tick-grey);
  }
  .ticks li::after {
    content: ""; position: absolute; left: 5px; top: 12px;
    width: 6px; height: 4px; border-left: 2px solid var(--navy); border-bottom: 2px solid var(--navy);
    transform: rotate(-45deg);
  }
  .ticks li.plain::before, .ticks li.plain::after { display: none; }
  .ticks.light li::before { background: var(--white); }
  .ticks.light li::after { border-color: var(--gold); }
  .ticks.light-sky li::before { background: var(--white); }
  .ticks.light-sky li::after { border-color: var(--sky); }
  .ticks.light li, .ticks.light-sky li { color: var(--white); }

  .stat { display: flex; align-items: center; gap: 16px; }
  .stat-big { color: var(--white); font-weight: 600; line-height: .9; letter-spacing: -4px; }
  .stat-note { font-size: 26px; line-height: 29px; letter-spacing: -.4px; }

  .skyline { background: var(--gold-deep); }
  .panel-gold { background: var(--gold); }
  .panel-title {
    color: var(--white); font-weight: 600; font-size: 40px; line-height: 1; letter-spacing: -.5px;
  }

  .big-heading {
    color: var(--white); font-weight: 700; font-size: 82px; line-height: 1;
    letter-spacing: -1px; text-transform: uppercase;
  }
  .heading-saved { transform: scaleX(0.85); }
  .heading-overall { transform: scaleX(0.83); }

  .overall-art { left: 0; top: 2230px; }
  .fact-big { color: var(--white); font-weight: 700; font-size: 118px; line-height: 1; letter-spacing: -3px; }
  .fact-note { color: var(--white); font-size: 25px; line-height: 28px; letter-spacing: -.4px; }
  .icon-spot { border-radius: 50%; background: var(--white); }
</style>
</head>
<body>

  <h1>
    <span class="abs condensed title-main">Investing in your</span>
    <span class="abs condensed title-sub">20'S, 30'S, 40'S, 50'S AND 60'S</span>
  </h1>

  <!-- 20s -->
  <section class="abs" style="left:30px; top:380px; width:540px;">
    <div class="stage-head" style="margin-left:14px;">
      <div class="stage-icon" role="img" aria-label="Icon of a person holding a money bag"></div>
      <h2 class="stage-title">Investing in your 20's</h2>
    </div>
    <ul class="ticks" style="margin-top:12px;">
      <li>Start saving</li>
      <li>Start first retirement account</li>
    </ul>
    <div class="stat" style="margin:-4px 0 2px;">
      <span class="stat-big" style="font-size:112px;">15%</span>
      <span class="stat-note">Set aside 15% of income in<br>retirement account</span>
    </div>
    <ul class="ticks">
      <li>Learn compound interest</li>
      <li>Understand matching 401(k) - average 401k employer contributions growing</li>
    </ul>
  </section>

  <!-- 30s -->
  <section class="abs" style="left:598px; top:380px; width:590px;">
    <div class="stage-head" style="margin-left:2px;">
      <div class="stage-icon" role="img" aria-label="Icon of a person holding a coin bag"></div>
      <h2 class="stage-title">Investing in your 30's</h2>
    </div>
    <ul class="ticks" style="margin-top:12px;">
      <li>Build emergency fund of 3-6 months worth of expenses</li>
      <li>Increase retirement contributions</li>
      <li>Have equivalent of annual salary saved by age 30</li>
    </ul>
    <div class="stat" style="margin:0 0 6px;">
      <span class="stat-big" style="font-size:112px; width:112px;">2X</span>
      <span class="stat-note" style="margin-left:4px;">Have twice annual salary saved by<br>age 35</span>
    </div>
    <ul class="ticks">
      <li>Increase finance knowledge - Understand difference between various investment funds(mutual fund, etf, index)</li>
    </ul>
  </section>

  <!-- 40s -->
  <section class="abs" style="left:30px; top:792px; width:560px;">
    <div class="stage-head">
      <div class="stage-icon" role="img" aria-label="Icon of hands holding a growing coin plant"></div>
      <h2 class="stage-title">Investing in your 40's</h2>
    </div>
    <ul class="ticks" style="margin-top:14px;">
      <li>Diversify investments</li>
      <li>Keep investment fees low</li>
      <li>Reduce or eliminate debt</li>
      <li>Have 3x your annual salary saved by 40 and 4x by 45</li>
    </ul>
  </section>

  <!-- 50s -->
  <section class="abs" style="left:598px; top:792px; width:560px;">
    <div class="stage-head">
      <div class="stage-icon" role="img" aria-label="Icon of a handshake inside a heart"></div>
      <h2 class="stage-title">Investing in your 50's</h2>
    </div>
    <ul class="ticks" style="margin-top:14px;">
      <li>Avoid new debt</li>
      <li>Take advantage of retirement catch-ups (differences between 401k, IRAs, and HSA)</li>
    </ul>
  </section>

  <!-- Savings band -->
  <div class="abs skyline" style="left:0; top:1070px; width:590px; height:90px;" role="img" aria-label="City skyline silhouette in gold"></div>
  <div class="abs" style="left:590px; top:1080px; width:610px; height:90px; background:#0aa2dd;" role="img" aria-label="City skyline silhouette in blue"></div>
  <div class="abs panel-gold" style="left:0; top:1155px; width:600px; height:298px;" role="img" aria-label="Photo of gold bars and coins on a table"></div>
  <svg class="abs" style="left:0; top:1150px;" width="1200" height="322" viewBox="0 0 1200 322" aria-hidden="true">
    <polygon points="592,5 1200,5 1200,322 548,322" fill="var(--sky)"/>
  </svg>

  <section class="abs" style="left:28px; top:1200px; width:540px;">
    <div class="stage-head" style="gap:12px;">
      <div class="icon-spot" style="width:70px; height:58px; border-radius:40%;" role="img" aria-label="Icon of a hand holding a money bag"></div>
      <h3 class="panel-title">63,000 SAVED IN 40'S</h3>
    </div>
    <ul class="ticks light" style="margin-top:18px;">
      <li>Average american has 4k in liquid savings and 63k in retirement funds</li>
    </ul>
  </section>

  <section class="abs" style="left:598px; top:1200px; width:560px;">
    <div class="stage-head" style="gap:12px;">
      <div class="icon-spot" style="width:72px; height:72px;" role="img" aria-label="Icon of a money bag with a clock"></div>
      <h3 class="panel-title">6X-8X SALARY SAVED</h3>
    </div>
    <ul class="ticks light-sky" style="margin-top:14px;">
      <li>Have 6x-8x annual salary saved by retirement</li>
      <li>Average American has 5k in liquid savings &amp; 117k in retirement funds</li>
      <li>Dont remove investments from stocks too much, but diversify further</li>
    </ul>
  </section>

  <!-- 250,000 -->
  <section class="abs" style="left:30px; top:1535px; width:1140px;">
    <h2 class="big-heading condensed heading-saved">250,000? IS WHAT SHOULD BE SAVED</h2>
    <ul class="ticks" style="margin-top:34px;">
      <li>Use HSA or FSA accounts</li>
      <li>Life insurance bought and understood</li>
    </ul>
  </section>

  <!-- 60s -->
  <section class="abs" style="left:30px; top:1765px; width:1140px;">
    <div class="stage-head">
      <div class="stage-icon" role="img" aria-label="Icon of a hand holding coins of different currencies"></div>
      <h2 class="stage-title">Investing in your 60's</h2>
    </div>
    <div class="stat" style="margin:6px 0 8px;">
      <span class="stat-big" style="font-size:124px;">10X</span>
      <span class="stat-note" style="margin-left:6px;">Stay the course - Have 8x annual salary by 60 and 10x by 67</span>
    </div>
    <ul class="ticks">
      <li>Average american has 8k in liquid savings and median retirement account value of 172k</li>
      <li>Average social security benefit is only 1.4k (Need more SSA info Dana)</li>
      <li>Understand required minimum distribution (RMD) - differences between 401k and IRAs</li>
      <li>Life expectancy and preparing for that</li>
      <li style="margin-bottom:0;">May need to work longer</li>
      <li class="plain">Downsize</li>
    </ul>
  </section>

  <!-- Overall -->
  <svg class="abs overall-art" width="1200" height="631" viewBox="0 0 1200 631" aria-hidden="true">
    <polygon points="28,118 927,118 28,631" fill="var(--sky)"/>
    <polygon points="1166,10 1166,521 266,521" fill="var(--gold)"/>
  </svg>
  <div class="abs" style="left:770px; top:2330px; width:390px; height:420px; background:linear-gradient(160deg, rgba(255,255,255,.06), rgba(0,0,0,.04)); clip-path:polygon(100% 0,100% 100%,0 100%);" role="img" aria-label="Faded photo of a laptop and phone on a desk"></div>

  <h2 class="abs big-heading condensed heading-overall" style="left:30px; top:2238px;">OVERALL INVESTING INFORMATION</h2>

  <div class="abs fact-big" style="left:54px; top:2372px;">56%</div>
  <p class="abs fact-note" style="left:291px; top:2392px; width:360px;">Of households currently have money in an employer-sponsored retirement account (including pensions, 401(k)s, and others).</p>
  <div class="abs icon-spot" style="left:84px; top:2520px; width:195px; height:190px; border-radius:30%;" role="img" aria-label="Icon of a person beside a dollar coin"></div>

  <div class="abs icon-spot" style="left:890px; top:2418px; width:192px; height:170px; border-radius:40%;" role="img" aria-label="Icon of a dollar coin in front of a coin stack"></div>
  <div class="abs fact-big" style="left:540px; top:2620px;">35%</div>
  <p class="abs fact-note" style="left:777px; top:2660px; width:340px;">Americans don't participate in any retirement savings plan at all.</p>

</body>
</html>
```